CaptainKettle needs a new packaging

We are Coffee Roasters based in Versailles France.

We want a new design for our coffee packaging. The packaging is a basic brown paper bag. We are sticking on it a 99.1mm x 67.7mm Label.

We want a new design for the label. The label should have the following info : Name of the coffee, origin, one line of description, our website www.captainkettle.fr.

Enclosed you will find our logo, as well as a picture of our current packaging

The Design should be "simple yet sophisticate".

```html
<!DOCTYPE html>
<html lang="fr">
<head>
<meta charset="utf-8">
<title>CaptainKettle – Étiquette No5</title>
<link rel="stylesheet" href="https://fonts.googleapis.com/css2?family=Josefin+Sans:wght@400&family=Josefin+Slab:wght@400;600&family=Open+Sans:wght@400&display=swap">
<style>
  :root {
    --page: #ffffff;
    --paper: #ffffff;
    --roast-dark: #3a1f08;
    --roast-mid: #5b3810;
    --ink: #3a2412;
    --ink-soft: #4a3525;
    --cream: #ffffff;
    --bean-dark: #3b2213;
    --bean-mid: #7a4a26;
    --bean-light: #a8704a;
  }
  * { margin: 0; padding: 0; box-sizing: border-box; }
  html, body {
    width: 1200px; height: 1000px; overflow: hidden;
    background: var(--page);
  }
  .canvas {
    position: relative; width: 1200px; height: 1000px;
  }
  .label {
    position: absolute; left: 100px; top: 160px;
    width: 1000px; height: 680px;
    background: var(--paper);
    overflow: hidden;
    box-shadow: 6px 8px 18px rgba(0,0,0,0.35);
  }
  .brand-band {
    position: absolute; left: 0; top: 33px; width: 100%; height: 228px;
    background: radial-gradient(ellipse 40% 90% at 45% 0%, var(--roast-mid), var(--roast-dark) 70%);
  }
  .brand-dot {
    position: absolute; left: 174px; top: 44px;
    width: 140px; height: 140px; border-radius: 50%;
    background: var(--cream);
  }
  .brand-name {
    position: absolute; left: 338px; top: 52px;
    font-family: "Josefin Sans", sans-serif; font-weight: 400;
    font-size: 86px; line-height: 1; color: var(--cream);
    letter-spacing: 0.5px;
  }
  .brand-tagline {
    position: absolute; left: 338px; top: 160px;
    font-family: "Josefin Sans", sans-serif; font-weight: 400;
    font-size: 32px; line-height: 1; color: var(--cream);
  }
  .beans {
    position: absolute; left: 0; bottom: 0; width: 100%; height: 240px;
    background:
      linear-gradient(to bottom, var(--paper) 0%, rgba(255,255,255,0) 55%),
      linear-gradient(to right, var(--bean-dark), var(--bean-mid) 20%, var(--bean-light) 50%, var(--bean-mid) 80%, var(--bean-dark));
  }
  .product {
    position: absolute; left: 0; top: 275px; width: 100%;
    text-align: center; color: var(--ink);
  }
  .product-name {
    font-family: "Josefin Slab", serif; font-weight: 600;
    font-size: 78px; line-height: 1;
  }
  .product-blend, .product-origin {
    font-family: "Josefin Slab", serif; font-weight: 600;
    font-size: 36px; line-height: 1.15;
  }
  .product-blend { margin-top: 6px; }
  .product-description {
    font-family: "Open Sans", sans-serif; font-size: 25px;
    color: var(--ink-soft); margin-top: 20px;
  }
  .contact {
    position: absolute; left: 0; top: 538px; width: 100%;
    text-align: center; color: var(--ink);
    font-family: "Open Sans", sans-serif; font-size: 19px; line-height: 1.3;
  }
  .contact .sep { margin: 0 10px; }
</style>
</head>
<body>
  <main class="canvas">
    <section class="label">
      <div class="beans" role="img" aria-label="Photographie de grains de café torréfiés en bas de l'étiquette"></div>
      <header class="brand-band">
        <span class="brand-dot"></span>
        <p class="brand-name">CaptainKettle</p>
        <p class="brand-tagline">Artisan Torréfacteur</p>
      </header>
      <div class="product">
        <h1 class="product-name">No5 de CaptainKettle</h1>
        <p class="product-blend">100% Arabica</p>
        <p class="product-origin">(Brésil, Congo, Ethiopie)</p>
        <p class="product-description">Description placed here</p>
      </div>
      <footer class="contact">
        <p>14 rue des Tilleuls 78000 Versailles<span class="sep">|</span>Tel. +33 1 00 00 00 00</p>
        <p>captainkettle.fr</p>
      </footer>
    </section>
  </main>
</body>
</html>
```